Traineeship Flyer Design Project

Requirements:
• 1 x A4 page flyer (double sided)
1st page; target market 15-19 yr old, looking for young/fresh, exciting, eye catching
2nd page: same look/feel – target market – parents/person to determine if there is value to devoting energy to this qualification (potentially less busy in design)
• Use of high quality logos: 1. Quandrel 2. Nationally recognised training logo
Ideally wanting to keep amount of copy to the page layout as attached, although designer is free to interpret the layout of copy on each page, although Quandrel will accept alternative presentation if designer sees new way to combine information
• Quandrel does not have a set colour palette so there are no restrictions/guidelines to follow
Updates
Hi, All files including brief and logos have now been updated.
Reason: Hi everyone
Please refer to design submission below for the only design that was deemed to cover off on the brief as the starting point - in regards to producing a design that appeals to target market of young person (15-19) in regards to self selecting to take up further study
Hi everyone
Can you please view the 3 remaining designs that are in contention (out of 30+ submitted) - Design 1528020 ; 1510098; 1510087; I will be providing additional feedback to these designers, as that come closer to the mark of appealing to younger "potential trainee" - the collateral needs to make the young student want to pick up the flyer (eye catching/interesting) and then be motivated to want to self elect - "beg parents" to take up the option. **PLEASE NOTE - I have uploaded a colour swatch now, and would appreciate if desgins could use these colours (not a requirement to use base colours of blue a silver as base if an exciting image needs to come from leaning on "secondary colours" (brighter) as being the predominant colours.
Many thanks, appreciate being able to see such an active community of designers involved in this website
Target Market(s)
1st page; target market 15-19 yr old, looking for young/fresh, exciting, eye catching. same look/feel – target market – parents/person to decide on
Industry/Entity Type
Training
Look and feel

```html
<!DOCTYPE html>
<html lang="en">
<head>
<meta charset="utf-8">
<title>Quandrel National Traineeships</title>
<link rel="stylesheet" href="https://fonts.googleapis.com/css2?family=Roboto+Condensed:wght@400;700;900&family=Source+Sans+3:wght@400;600;700;900&display=swap">
<style>
  :root {
    --navy: #0f2a52;
    --navy-deep: #081a38;
    --white: #ffffff;
    --lime: #d8ec5a;
    --green: #5bb432;
    --orange: #f26522;
    --blue: #1e8ad6;
    --purple: #7b3f98;
    --grey: #8a8f98;
    --red: #d7262e;
    --ink-blue: #1d4f96;
    --pin: #2b6fb3;
    --paper: #f4f6f8;
  }
  * { margin: 0; padding: 0; box-sizing: border-box; }
  html, body { width: 851px; height: 1200px; overflow: hidden; background: var(--navy-deep); }
  body { font-family: "Source Sans 3", Arial, sans-serif; }

  .flyer {
    position: relative; width: 851px; height: 1200px; overflow: hidden;
    background: linear-gradient(180deg, #1a3f73 0%, var(--navy) 45%, var(--navy-deep) 100%);
  }

  .hero-photo {
    position: absolute; right: 0; top: 40px; width: 500px; height: 530px;
    background:
      linear-gradient(90deg, var(--navy) 0%, rgba(15,42,82,0) 30%),
      linear-gradient(0deg, var(--navy) 0%, rgba(15,42,82,0) 25%),
      radial-gradient(ellipse at 62% 50%, #e9c2a6 0%, #c98e6f 30%, #6b4a3a 60%, #243f66 100%);
  }

  .masthead {
    position: absolute; left: 0; top: 0; width: 851px; height: 112px;
    background: var(--white);
    clip-path: polygon(0 0, 100% 0, 100% 70%, 0 100%);
  }
  .brand {
    position: absolute; left: 44px; top: 30px;
    display: flex; align-items: center; gap: 12px;
    color: var(--navy); font-weight: 600; font-size: 42px; letter-spacing: 0.5px;
  }
  .brand-mark { width: 34px; height: 34px; background: var(--navy); }

  .headline {
    position: absolute; left: 43px; top: 246px;
    color: var(--white); font-family: "Roboto Condensed", Arial, sans-serif;
    font-weight: 700; font-size: 64px; line-height: 0.98; letter-spacing: -0.5px;
  }
  .tagline {
    position: absolute; left: 43px; top: 396px; width: 340px;
    color: var(--lime); font-family: "Roboto Condensed", Arial, sans-serif;
    font-weight: 700; font-size: 35px; line-height: 38px;
  }

  .steps { position: absolute; left: 397px; top: 559px; width: 426px; list-style: none; }
  .step {
    display: flex; height: 40px; margin-bottom: 20px;
    color: var(--white); font-family: "Roboto Condensed", Arial, sans-serif;
    font-weight: 700; text-transform: uppercase;
  }
  .step-num {
    width: 110px; display: flex; align-items: center; padding-left: 16px;
    font-size: 19px; text-transform: none; background: rgba(0,0,0,0.18);
  }
  .step-label { flex: 1; display: flex; align-items: center; justify-content: center; font-size: 19px; }
  .step--1 { background: var(--orange); }
  .step--2 { background: var(--blue); }
  .step--3 { background: var(--purple); }
  .step--4 { background: var(--green); }
  .step--5 { background: var(--grey); }
  .step--6 { background: var(--red); }

  .note {
    position: absolute; left: 50px; top: 622px; width: 270px; height: 260px;
    background: var(--paper); transform: rotate(-6deg);
    box-shadow: 4px 6px 12px rgba(0,0,0,0.45);
    padding: 36px 16px 0;
    color: var(--ink-blue); text-align: center;
    font-family: "Roboto Condensed", Arial, sans-serif;
    font-weight: 700; font-size: 27px; line-height: 1.02;
  }
  .note strong { font-size: 44px; font-weight: 900; display: block; line-height: 1; }
  .note-pin { position: absolute; left: 122px; top: -14px; }

  .careers-tab {
    position: absolute; left: 0; top: 1050px; width: 241px; height: 58px;
    background: var(--green); color: var(--white);
    font-family: "Roboto Condensed", Arial, sans-serif;
    font-weight: 700; font-size: 20px; line-height: 1.05;
    display: flex; align-items: center; padding-left: 22px;
    clip-path: polygon(0 0, 92% 0, 100% 50%, 92% 100%, 0 100%);
  }
  .careers {
    position: absolute; left: 255px; top: 988px; list-style: none;
    color: var(--white); font-family: "Roboto Condensed", Arial, sans-serif;
    font-size: 19px; font-weight: 700; line-height: 29px; white-space: nowrap;
  }
  .careers li::before {
    content: ""; display: inline-block; width: 8px; height: 8px; margin-right: 12px;
    background: var(--green); border-radius: 50%; vertical-align: middle;
  }

  .cost { position: absolute; left: 596px; top: 944px; width: 236px; color: var(--white); }
  .cost-title {
    display: flex; align-items: center; gap: 6px; white-space: nowrap;
    font-family: "Roboto Condensed", Arial, sans-serif;
    font-weight: 900; font-size: 27px; line-height: 0.95;
  }
  .cost-q { font-size: 58px; line-height: 1; }
  .cost-answer {
    color: var(--orange); font-weight: 600; font-size: 34px; line-height: 1;
    margin: 8px 0 6px; text-align: right;
  }
  .cost-body { font-size: 19px; line-height: 1.12; text-align: right; }
  .cost-body em { font-style: normal; font-weight: 700; font-size: 22px; }
</style>
</head>
<body>
<main class="flyer">
  <div class="hero-photo" role="img" aria-label="Photograph of a smiling young woman, the featured trainee"></div>

  <header class="masthead">
    <div class="brand"><span class="brand-mark"></span><span>Quandrel</span></div>
  </header>

  <h1 class="headline">National<br>Traineeships</h1>
  <p class="tagline">Kick-start your<br>career today for free!<br>Get ahead of the game<br>Learn on the job.</p>

  <ol class="steps">
    <li class="step step--1"><span class="step-num">Step 1</span><span class="step-label">Information session</span></li>
    <li class="step step--2"><span class="step-num">Step 2</span><span class="step-label">Register your interest</span></li>
    <li class="step step--3"><span class="step-num">Step 3</span><span class="step-label">Enrolment</span></li>
    <li class="step step--4"><span class="step-num">Step 4</span><span class="step-label">Start training</span></li>
    <li class="step step--5"><span class="step-num">Step 5</span><span class="step-label">Practical assessments</span></li>
    <li class="step step--6"><span class="step-num">Step 6</span><span class="step-label">Graduate</span></li>
  </ol>

  <aside class="note">
    <svg class="note-pin" width="26" height="34" viewBox="0 0 26 34" aria-hidden="true">
      <circle cx="13" cy="11" r="10" fill="var(--pin)"/>
      <rect x="12" y="19" width="2" height="14" fill="#666"/>
    </svg>
    Gain a formal
    <strong>national</strong>
    qualification recognised by all employers Australia wide.
  </aside>

  <div class="careers-tab">Excellent possible<br>career choices</div>
  <ul class="careers">
    <li>Accounts Clerk</li>
    <li>Office Administrator</li>
    <li>Senior sales assistant</li>
    <li>Merchandise manager</li>
    <li>Customer service manager</li>
    <li>Small business retail owner</li>
  </ul>

  <section class="cost">
    <div class="cost-title"><span class="cost-q">?</span><span>How much<br>will it cost</span><span class="cost-q">?</span></div>
    <p class="cost-answer">Nothing!</p>
    <p class="cost-body">The full course is provided by <em>your employer</em>. No prior training or <em>experiences</em> required.</p>
  </section>
</main>
</body>
</html>
```